Creative, fresh business card design for Brindlecrest Linings

We need a fresh, creative business card design for Brindlecrest Linings. We are the manufacturer of Brindlecrest Linings in Australia. Wall panels are 2400 x 1200mm panels made from MDF and feature 3D patterns on the face of the panel. The colours to be used are green, silver/grey and white RGB
Red 187
Green 207
Blue 65.

An idea is to possibly use a watermark of one of our designs as a background (like on the "Lattice" design on the left hand side of page 2 of our brochure).

Target Market(s)

Interior designers, architects, builders and home renovators

Industry/Entity Type

Business

Contact Information for Business Card

Details to go on the card are:
Our logo (attached),
Slogan: "Decorative panels for interiors and exteriors",
Contact name,
Position,
Mobile phone number,
Business address,
Business phone,
Business fax,
Website and
Email address.

I have attached a few images of our panels and our brochure for reference.

The colours of the business card should feature our logo colours which are: RGB
Red 187
Green 207
Blue 65

Requirements
Must have
• Very modern fonts and design. Some of the designs shown especially the "Weave" design which is a popular design.
Nice to have
• Creative but simple design. Very contemporary.
Should not have
• Anything ornate or old fashioned.

```html
<!DOCTYPE html>
<html lang="en">
<head>
<meta charset="utf-8">
<title>Brindlecrest Linings – Business Card</title>
<link rel="stylesheet" href="https://fonts.googleapis.com/css2?family=Montserrat:wght@700&family=Lora:wght@400&display=swap">
<style>
  :root {
    --brand-green: rgb(187, 207, 65);
    --green-text: #7e9422;
    --silver: #a3a4a6;
    --silver-light: #e9eaec;
    --ink: #1c1c1c;
    --paper: #ffffff;
    --backdrop: #2b2b2d;
  }
  * { box-sizing: border-box; margin: 0; padding: 0; }
  html, body { width: 1200px; height: 1200px; overflow: hidden; }
  body {
    background: var(--backdrop);
    display: flex;
    flex-direction: column;
    align-items: center;
    justify-content: center;
    gap: 50px;
  }
  .card {
    position: relative;
    width: 900px;
    height: 514px;
    overflow: hidden;
    background: var(--paper);
  }

  /* Front */
  .front-photo {
    position: absolute; inset: 0;
    background: linear-gradient(120deg, #c8564f 0%, #d9726a 30%, #e8d9c8 52%, #b58a3c 70%, #7a6d8e 85%, #5c8a8e 100%);
  }
  .brand-plate {
    position: absolute;
    left: 50%; top: 50%;
    transform: translate(-50%, -50%);
    background: var(--paper);
    padding: 34px 44px;
    display: flex;
    align-items: center;
    gap: 18px;
    white-space: nowrap;
  }
  .brand-mark {
    flex: none;
    width: 36px; height: 36px;
    background: var(--brand-green);
  }
  .brand-name {
    font-family: "Montserrat", sans-serif;
    font-weight: 700;
    font-size: 36px;
    color: var(--brand-green);
  }

  /* Back */
  .panel-texture {
    position: absolute; inset: 0;
    background: linear-gradient(170deg, #ffffff 0%, var(--silver-light) 45%, #f7f7f8 70%, #e4e5e7 100%);
  }
  .rule { position: absolute; left: 0; right: 0; height: 2px; background: var(--ink); }
  .rule-top { top: 38px; }
  .name-band {
    position: absolute; left: 0; right: 0; top: 48px; height: 104px;
    background: var(--brand-green);
    display: flex; align-items: center; justify-content: center; gap: 18px;
  }
  .rule-band { top: 156px; }
  .contact-name {
    font-family: "Montserrat", sans-serif;
    font-weight: 700; font-size: 38px; letter-spacing: -0.5px;
    color: var(--ink);
  }
  .divider { width: 2px; height: 40px; background: var(--ink); }
  .position {
    font-family: "Lora", serif; font-size: 26px; color: var(--ink);
  }
  .contact {
    position: absolute; left: 0; right: 0; top: 188px;
    text-align: center;
    font-family: "Lora", serif; font-size: 26px; color: var(--ink);
    line-height: 1.75;
  }
  .contact .label { color: var(--green-text); }
  .contact .address { margin-top: 22px; }
  .contact .hairline {
    width: 520px; height: 1px; margin: 4px auto 2px;
    background: var(--silver);
  }
  .rule-bottom { top: 418px; }
  .slogan-band {
    position: absolute; left: 0; right: 0; bottom: 0; height: 86px;
    background: var(--silver);
    display: flex; align-items: center; justify-content: center;
    font-family: "Lora", serif; font-size: 27px; letter-spacing: 5px;
    color: var(--paper);
    white-space: nowrap;
  }
</style>
</head>
<body>
  <section class="card card-front">
    <div class="front-photo" role="img" aria-label="Interior photograph of a red faceted wall panel beside shelving with coloured glass vases"></div>
    <div class="brand-plate">
      <span class="brand-mark"></span>
      <span class="brand-name">Brindlecrest Linings</span>
    </div>
  </section>

  <section class="card card-back">
    <div class="panel-texture" role="img" aria-label="Faint white wall panel texture with flowing wave-shaped ridges"></div>
    <div class="rule rule-top"></div>
    <div class="name-band">
      <span class="contact-name">MARCUS HALE</span>
      <span class="divider"></span>
      <span class="position">Director</span>
    </div>
    <div class="rule rule-band"></div>
    <div class="contact">
      <p><span class="label">M:</span> 0412 583 906</p>
      <p><span class="label">T:</span> 02 8631 5190 | <span class="label">F:</span> 02 8631 5191</p>
      <p class="address">14 Calloway Road, Kelmscott Park NSW 2170</p>
      <div class="hairline"></div>
      <p>sales@brindlecrest.com.au | www.brindlecrest.com.au</p>
    </div>
    <div class="rule rule-bottom"></div>
    <div class="slogan-band">Decorative panels for interiors and exteriors</div>
  </section>
</body>
</html>
```